Internation Biosecurity Business that needs a to design a Label for Itch relief product

Brand Name: Harbor Dermis
I have a logo.
Label sign is 2.5 x 5.5
Label will be printed on clear vinyl.
The bottle to receive this label is colour of white.

I like the look of a label with the bottom starting off as a solid colour and transitioning to white at the top. But if you have something else you would like to try I am going to be open to it.
What ever colours and design you create it must reflect a natural, clean, soothing feeling. This colour could stop on the main panel or continue across to the side panel.
Primary panel size 2.5 x 3, Back side panel size 2.5 x 2.5 for a total size of 2.5 x 5.5 inches
Text on primary panel:
logo (which will have the brand name Harbor Dermis incorporated in it)
- Itch Relief (main message to stand out big ! )
- from Psoriasis, Eczema, Dermatitis (secondary message) but also must stand out but less than "Itch Relief"
- Natural, Nontoxic, Non- medicated (place at bottom
- 100ml (Bottle size)
I am looking for a symbol to be in the background on the main panel or as a water mark on the back panel. This symbol will have a very light outline so it hardly noticed. The symbol I had in mind was the "Harbor Bell" because it stands for freedom. My hope is this will convey a subliminal message of freedom, liberty and trust. You can be free to select a different symbol or nothing at all.

The logo that I have attached Harbor Dermis but these colours must be changed to new colours which must harmonize with the colour you select for the over all label.
I will be coming out with many more labels in this "Harbor" line so the designer that creates the winning art work will be hired in the not-so- distant future for all new labels.
The product is water based and sprayed on. Active ingredient is HOCL. You cannot harm yourself even if it get in your eyes. Our products comes at treating the problems from a Holistic approach and not from a chemical medicated approach.
Company Name: PuraKleen Systems Inc. Box 4087, Innisfail Alberta, T9K 3M2 1 800-517 -2946 Made in Canada (UPC Code: 6 51920 48163 2)

Industry/Entity Type

Business

Colors
886aae
b7a5cd
e4daeb

Requirements
Must have
• Final Graphic files must be in vector/eps format! I need you to enlarge it more because I can not read or see label text or see how you have placed the bell even at the 150%. The situation is that I will be using the winning design as a template for Harbor Peak, Harbor Dermis and Harbor Vita. Each of these categories may have 2 - 4 different products in them. What will distinguished these categories will be a different colour at the bottom of the label. For the Harbor Dermis label I have chosen the mauve or light purple. Light green of Harbor Peak, Light blue for Harbor Vita.
• At the bottom of the label let remove "Antimicrobial Cleanser". One of the problems we Canada's manufacturers have is that some keg words on our labels mush me in French and your present design does not lend itself to incorporating French. We may be able to have a French label underneath the English label, However, The words "Itch Relief" and the phase "Natural, Nontoxic, Non-Medicated" would need to be in French, at a reduced size, so we may need some space. French for Itch Relief is: D mangeaison de secours (place very small under "Itch Relief") French for Natural, Nontoxic, Non-medicated is : Naturel, Non toxque, Non meddicamenteux, place very small under the English.
Should not have
• The same colours that are in the Harbor Dermis Logo. I want different colours.

```html
<!DOCTYPE html>
<html lang="en">
<head>
<meta charset="utf-8">
<title>Harbor Dermis Itch Relief Label</title>
<link href="https://fonts.googleapis.com/css2?family=Roboto+Condensed:wght@700;900&family=Play:wght@700&family=Noto+Sans:wght@400;700&display=swap" rel="stylesheet">
<style>
  :root {
    --backdrop: #e5e6e8;
    --paper: #ffffff;
    --mauve-deep: #7a5c99;
    --mauve: #886aae;
    --mauve-light: #b7a5cd;
    --mauve-pale: #e4daeb;
    --badge: #6f5a93;
    --brand-green: #0f5a3a;
    --brand-mint: #8fd0b5;
    --ink: #111111;
    --placeholder: #e4e5e7;
    --crop: #111111;
    --crop-centre: #c0392b;
  }
  html, body {
    margin: 0;
    padding: 0;
    width: 1200px;
    height: 1000px;
    overflow: hidden;
    background: var(--backdrop);
  }
  .canvas {
    position: relative;
    width: 1200px;
    height: 1000px;
  }
  .crop-marks {
    position: absolute;
    inset: 0;
  }
  .label {
    position: absolute;
    left: 93px;
    top: 246px;
    width: 1014px;
    height: 507px;
    background: var(--paper);
  }
  /* primary panel */
  .brand {
    position: absolute;
    left: 120px;
    top: 56px;
    display: flex;
    align-items: center;
    gap: 12px;
  }
  .brand-square {
    width: 44px;
    height: 44px;
    background: var(--brand-mint);
  }
  .brand-name {
    font-family: "Noto Sans", sans-serif;
    font-weight: 700;
    font-size: 34px;
    color: var(--brand-green);
    letter-spacing: 0.5px;
  }
  .title-rule {
    position: absolute;
    left: 147px;
    width: 215px;
    height: 3px;
    background: linear-gradient(90deg, rgba(183,165,205,0), var(--mauve-light) 50%, rgba(183,165,205,0));
  }
  .title-rule.top { top: 150px; }
  .title-rule.bottom { top: 214px; }
  .product-title {
    position: absolute;
    left: 0;
    width: 507px;
    top: 150px;
    margin: 0;
    text-align: center;
    font-family: "Roboto Condensed", sans-serif;
    font-weight: 900;
    font-size: 62px;
    line-height: 64px;
    color: var(--mauve-deep);
    letter-spacing: 1.5px;
  }
  .product-title-fr {
    position: absolute;
    left: 0;
    width: 507px;
    top: 219px;
    margin: 0;
    text-align: center;
    font-family: "Roboto Condensed", sans-serif;
    font-weight: 700;
    font-size: 14px;
    line-height: 18px;
    color: var(--mauve-deep);
    letter-spacing: 0.5px;
  }
  .conditions-band {
    position: absolute;
    left: 0;
    top: 241px;
    width: 507px;
    height: 165px;
    background: radial-gradient(ellipse 60% 90% at 48% 10%, #b9a6d0 0%, #a088c0 45%, var(--mauve) 100%);
  }
  .conditions-divider {
    position: absolute;
    left: 93px;
    top: 21px;
    width: 2px;
    height: 122px;
    background: linear-gradient(180deg, rgba(255,255,255,0.2), #fff 50%, rgba(255,255,255,0.2));
  }
  .conditions {
    position: absolute;
    left: 108px;
    top: 24px;
    margin: 0;
    padding: 0;
    list-style: none;
    font-family: "Play", sans-serif;
    font-weight: 700;
    font-size: 32px;
    line-height: 40px;
    color: #ffffff;
  }
  .claims-band {
    position: absolute;
    left: 0;
    top: 406px;
    width: 507px;
    height: 62px;
    background: var(--mauve-light);
    text-align: center;
    color: #ffffff;
    font-family: "Roboto Condensed", sans-serif;
    font-weight: 700;
  }
  .claims {
    display: block;
    padding-top: 4px;
    font-size: 25px;
    line-height: 28px;
    text-shadow: 0 1px 2px rgba(80,60,110,0.35);
  }
  .claims-fr {
    display: block;
    font-size: 12px;
    line-height: 14px;
    letter-spacing: 0.3px;
  }
  .volume-badge {
    position: absolute;
    left: 207px;
    top: 451px;
    width: 92px;
    height: 33px;
    border-radius: 5px;
    background: var(--badge);
    color: #ffffff;
    font-family: "Play", sans-serif;
    font-weight: 700;
    font-size: 21px;
    line-height: 33px;
    text-align: center;
  }
  /* back panel */
  .info {
    position: absolute;
    left: 550px;
    top: 45px;
    width: 418px;
    margin: 0;
    font-family: "Noto Sans", sans-serif;
    font-size: 15.5px;
    line-height: 25px;
    letter-spacing: 0.3px;
    color: var(--ink);
  }
  .info strong { font-weight: 700; }
  .info-block { margin: 0; }
  .placeholder {
    position: absolute;
    top: 367px;
    height: 101px;
    background: var(--placeholder);
  }
  .placeholder.wide { left: 551px; width: 277px; }
  .placeholder.narrow { left: 846px; width: 124px; }
</style>
</head>
<body>
<div class="canvas">
  <svg class="crop-marks" width="1200" height="1000" viewBox="0 0 1200 1000" aria-hidden="true">
    <g stroke="var(--crop)" stroke-width="1.5">
      <line x1="93" y1="216" x2="93" y2="238"/>
      <line x1="63" y1="246" x2="85" y2="246"/>
      <line x1="1107" y1="216" x2="1107" y2="238"/>
      <line x1="1115" y1="246" x2="1137" y2="246"/>
      <line x1="93" y1="761" x2="93" y2="783"/>
      <line x1="63" y1="753" x2="85" y2="753"/>
      <line x1="1107" y1="761" x2="1107" y2="783"/>
      <line x1="1115" y1="753" x2="1137" y2="753"/>
    </g>
    <g stroke="var(--crop-centre)" stroke-width="1.5">
      <line x1="600" y1="216" x2="600" y2="238"/>
      <line x1="600" y1="761" x2="600" y2="783"/>
    </g>
  </svg>

  <section class="label">
    <div class="brand">
      <span class="brand-square"></span>
      <span class="brand-name">Harbor Dermis</span>
    </div>

    <div class="title-rule top"></div>
    <h1 class="product-title">ITCH RELIEF</h1>
    <div class="title-rule bottom"></div>
    <p class="product-title-fr" lang="fr">Démangeaison de secours</p>

    <div class="conditions-band">
      <div class="conditions-divider"></div>
      <ul class="conditions">
        <li>Psoriasis</li>
        <li>Eczema</li>
        <li>Dermatitis</li>
      </ul>
    </div>

    <div class="claims-band">
      <span class="claims">Natural. Nontoxic. Non-Medicated</span>
      <span class="claims-fr" lang="fr">Naturel. Non toxique. Non médicamenteux</span>
    </div>
    <div class="volume-badge">100ml</div>

    <div class="info">
      <p class="info-block"><strong>Objective</strong>:&nbsp; To effectively and painlessly provide fast relief.</p>
      <p class="info-block"><strong>Directions</strong>:&nbsp; Spray on affected area, repeat 2 – 4 times per day. In severe cases saturate clean bandage with Harbor Dermis Itch Relief and apply overnight. Keeping the area wet with Harbor Dermis will maximize performance. If area does not improve within seven days seek medical advice.</p>
      <p class="info-block"><strong>Product Care</strong>:&nbsp; Keep bottle sealed and at room temperature for optimum shelf life. Biodegradable.</p>
      <p class="info-block"><strong>Ingredients</strong>:&nbsp; Ionized water, Hypochlorous acid (HOCL) 50mg/L, Sodium Chloride 15mg/L.</p>
    </div>

    <div class="placeholder wide"></div>
    <div class="placeholder narrow"></div>
  </section>
</div>
</body>
</html>
```